Home Page Design

We have a B2B home page design and need a consumer version. The look and feel can look similar but needs to be distinctly different so it in not to get confused. Essentially it should look like the same company with a different model. We will need a PSD w all layers organized and easy to understand. Attached is the logo, B2B comp, and a MS Word doc with a short description. In addition, I have attached a wire frame to be used as a site map. PLEASE DO NOT take that as the creative. I expect to see your creative based on the information provided.

Industry/Entity Type

Consumer

```html
<!DOCTYPE html>
<html lang="en">
<head>
<meta charset="utf-8">
<title>GivingHost.com – Charity Auctions &amp; Events</title>
<link rel="stylesheet" href="https://fonts.googleapis.com/css2?family=Questrial&family=Catamaran:wght@600;700&display=swap">
<style>
:root{
  --blue:#1a6b96;
  --blue-dark:#0f4f72;
  --blue-band:rgba(26,107,150,.88);
  --green:#3cb74a;
  --panel:#eff0f2;
  --grey-box:#cfcfcf;
  --footer:#5b5b5b;
  --text:#444;
  --white:#fff;
}
*{box-sizing:border-box;margin:0;padding:0}
html,body{width:1121px;height:1200px;overflow:hidden}
body{position:relative;background:var(--white);font-family:"Questrial",sans-serif;color:var(--text)}
.abs{position:absolute}

/* header */
.site-header{left:0;top:0;width:1121px;height:90px}
.brand{left:82px;top:22px;display:flex;align-items:center;gap:10px;font-size:22px;color:var(--green)}
.brand-dot{width:44px;height:44px;border-radius:50%;background:var(--blue)}
.main-nav{right:84px;top:46px;display:flex;align-items:center;gap:40px;font-size:13px;color:#222}
.main-nav a{color:inherit;text-decoration:none}
.main-nav .cta{background:var(--blue);color:var(--white);padding:6px 14px;margin-right:-10px}

/* hero */
.hero{left:0;top:90px;width:1121px;height:392px;background:linear-gradient(120deg,#8b6a55 0%,#b88b6c 30%,#6e5647 55%,#a57c62 80%,#c9a488 100%)}
.hero-caption{left:182px;top:170px;width:751px;height:102px;background:rgba(40,40,40,.35);text-align:center;color:var(--white)}
.hero-caption h1{font-family:"Catamaran",sans-serif;font-weight:600;font-size:31px;margin-top:2px;text-shadow:0 1px 3px rgba(0,0,0,.4)}
.hero-caption p{font-family:Arial,sans-serif;font-size:11.5px;line-height:15px;padding:0 30px;margin-top:4px}

/* content panel */
.footer-band{left:0;top:1085px;width:1121px;height:115px;background:var(--footer)}
.content{left:80px;top:482px;width:961px;height:634px;background:var(--panel)}

/* search boxes */
.search-head{left:71px;width:239px;height:33px;background:var(--blue);color:var(--white);font-family:"Catamaran",sans-serif;font-weight:700;font-size:14px;padding:7px 0 0 22px}
.search-head::after{content:"";position:absolute;left:0;bottom:-9px;border-top:9px solid var(--blue-dark);border-left:9px solid transparent}
.search-body{left:80px;width:230px}
.search-body.auction{top:565px;height:195px;background:var(--green)}
.search-body.event{top:838px;height:229px;background:var(--grey-box)}
.field{position:absolute;left:18px;width:193px;height:28px;background:var(--white);font-size:13px;color:#333;padding:6px 8px}
.btn{position:absolute;left:122px;width:89px;height:29px;background:var(--blue);color:var(--white);font-family:"Catamaran",sans-serif;font-weight:700;font-size:15px;text-align:center;line-height:30px}

/* featured */
.section-title{left:354px;font-family:"Catamaran",sans-serif;font-weight:700;font-size:21px;letter-spacing:.5px;color:var(--blue)}
.card{position:absolute;width:157px}
.card .photo{position:absolute;left:0;top:0;width:157px;height:155px}
.auction-card .band{position:absolute;left:0;top:108px;width:157px;height:47px;background:var(--blue-band);color:var(--white);font-family:"Catamaran",sans-serif;font-weight:700;font-size:12.5px;line-height:15px;padding:7px 0 0 7px;text-transform:uppercase}
.auction-card .band.single{padding-top:23px}
.arrow{position:absolute;right:8px;top:20px;width:19px;height:19px}
.event-card .meta{position:absolute;left:0;top:123px;width:157px;height:32px;background:var(--blue-band);color:var(--white);font-family:Arial,sans-serif;font-size:8.5px;display:flex;align-items:center;gap:4px;padding-left:5px}
.event-card .meta svg{flex:none}
.event-card h3{position:absolute;top:172px;left:0;width:157px;font-family:"Catamaran",sans-serif;font-weight:700;font-size:11.5px;line-height:14px;color:#555;text-transform:uppercase;letter-spacing:.3px}
.event-card p{position:absolute;top:205px;left:0;width:157px;font-family:Arial,sans-serif;font-size:10px;line-height:13px;color:#555}

/* footer */
.footer-nav{left:91px;top:1140px;font-size:12px;color:var(--white);word-spacing:2px}
.footer-nav span{margin:0 18px}
.copyright{left:92px;top:1167px;font-family:Arial,sans-serif;font-size:11px;color:var(--white)}
.footer-brand{left:832px;top:1132px;display:flex;align-items:center;gap:10px;font-size:19px;color:var(--white)}
.footer-brand .brand-dot{width:52px;height:52px;background:var(--white)}
</style>
</head>
<body>

<header class="site-header abs">
  <div class="brand abs"><span class="brand-dot"></span>GivingHost.com</div>
  <nav class="main-nav abs">
    <a class="cta" href="#">POST YOUR EVENT</a>
    <a href="#">ADD AUCTION ITEMS</a>
    <a href="#">ABOUT</a>
    <a href="#">CONTACT</a>
  </nav>
</header>

<section class="hero abs" role="img" aria-label="Photo of a group of smiling children close to the camera">
  <div class="hero-caption abs">
    <h1>Lorem ipsum dolor sit amet</h1>
    <p>Lorem ipsum dolor sit amet, consectetur adipisicing elit, sed do eiusmod tempor incididunt ut labore et dolore magna aliqua. Ut enim ad minim veniam, quis nostrud exercitation ullamco laboris nisi ut aliquip ex ea commodo consequat.</p>
  </div>
</section>

<div class="footer-band abs"></div>
<main class="content abs"></main>

<!-- auction search -->
<div class="search-head abs" style="top:532px">Search for An Auction Item</div>
<form class="search-body auction abs">
  <div class="field" style="top:18px">Auction Type</div>
  <div class="field" style="top:60px">Auction Date</div>
  <div class="field" style="top:101px">Charity</div>
  <div class="btn" style="top:148px">Search</div>
</form>

<!-- event search -->
<div class="search-head abs" style="top:806px">Search for An Auction Item</div>
<form class="search-body event abs">
  <div class="field" style="top:19px">Event Type</div>
  <div class="field" style="top:60px">Event Date</div>
  <div class="field" style="top:102px">Event Location</div>
  <div class="field" style="top:143px">Event Name</div>
  <div class="btn" style="top:188px">Search</div>
</form>

<!-- featured auction items -->
<h2 class="section-title abs" style="top:523px">FEATURED AUCTION ITEMS</h2>

<div class="card auction-card" style="left:354px;top:573px">
  <div class="photo" role="img" aria-label="Photo of guests at a formal dinner" style="background:linear-gradient(160deg,#5a4a44,#2b2624 60%,#8a3a34)"></div>
  <div class="band">Dinner with<br>Marcus Reed
    <svg class="arrow" viewBox="0 0 20 20"><circle cx="10" cy="10" r="10" fill="#fff"/><path d="M5 10h9M10 6l4 4-4 4" stroke="#1a6b96" stroke-width="2.2" fill="none"/></svg></div>
</div>
<div class="card auction-card" style="left:525px;top:573px">
  <div class="photo" role="img" aria-label="Photo of three wine bottles" style="background:linear-gradient(90deg,#f2f2ee,#5e5a3a 30%,#4a1f26 50%,#d8cf8a 72%,#f4f4f0)"></div>
  <div class="band">Case of<br>Vista Hill Wine
    <svg class="arrow" viewBox="0 0 20 20"><circle cx="10" cy="10" r="10" fill="#fff"/><path d="M5 10h9M10 6l4 4-4 4" stroke="#1a6b96" stroke-width="2.2" fill="none"/></svg></div>
</div>
<div class="card auction-card" style="left:695px;top:573px">
  <div class="photo" role="img" aria-label="Photo of a road bicycle" style="background:linear-gradient(160deg,#ffffff,#dfe6ea 50%,#8fa8b8)"></div>
  <div class="band single">Ridgeline Bicycle
    <svg class="arrow" viewBox="0 0 20 20"><circle cx="10" cy="10" r="10" fill="#fff"/><path d="M5 10h9M10 6l4 4-4 4" stroke="#1a6b96" stroke-width="2.2" fill="none"/></svg></div>
</div>
<div class="card auction-card" style="left:866px;top:573px">
  <div class="photo" role="img" aria-label="Photo of a Paris street with classic buildings" style="background:linear-gradient(170deg,#d9d3c4,#b6a98e 45%,#6d6658)"></div>
  <div class="band">5 Days/ 4 Nights<br>in Paris France
    <svg class="arrow" viewBox="0 0 20 20"><circle cx="10" cy="10" r="10" fill="#fff"/><path d="M5 10h9M10 6l4 4-4 4" stroke="#1a6b96" stroke-width="2.2" fill="none"/></svg></div>
</div>

<!-- featured charity events -->
<h2 class="section-title abs" style="top:800px">FEATURED CHARITY EVENTS</h2>

<div class="card event-card" style="left:354px;top:845px">
  <div class="photo" role="img" aria-label="Photo of a country club clubhouse above a golf course" style="background:linear-gradient(180deg,#3e8ad0,#9cc3e6 30%,#c9b79e 50%,#3f6e36 80%)"></div>
  <div class="meta"><svg width="14" height="14" viewBox="0 0 14 14"><circle cx="7" cy="7.5" r="5.5" stroke="#fff" stroke-width="1.4" fill="none"/><path d="M7 4.5v3" stroke="#fff" stroke-width="1.4"/></svg>03 DEC 2013 <svg width="12" height="12" viewBox="0 0 12 12"><path d="M2 10l1-3 6-6 2 2-6 6z" fill="#fff"/></svg>LORE IPSUM</div>
  <h3>November 12 Palmcrest<br>Country Club</h3>
  <p style="top:208px">Lorem ipsum sed do dolore magna&nbsp; aliqua minim veniam,.</p>
</div>
<div class="card event-card" style="left:525px;top:845px">
  <div class="photo" role="img" aria-label="Photo of a green golf fairway with desert hills" style="background:linear-gradient(180deg,#7aa3c9,#6b8a5a 30%,#9cc43a 55%,#c29a4a 85%)"></div>
  <div class="meta"><svg width="14" height="14" viewBox="0 0 14 14"><circle cx="7" cy="7.5" r="5.5" stroke="#fff" stroke-width="1.4" fill="none"/><path d="M7 4.5v3" stroke="#fff" stroke-width="1.4"/></svg>03 DEC 2013 <svg width="12" height="12" viewBox="0 0 12 12"><path d="M2 10l1-3 6-6 2 2-6 6z" fill="#fff"/></svg>LORE IPSUM</div>
  <h3>November 16 Shoreline<br>Dunes</h3>
  <p style="top:208px">Lorem ipsum sed do dolore magna&nbsp; aliqua minim veniam,.</p>
</div>
<div class="card event-card" style="left:695px;top:845px">
  <div class="photo" role="img" aria-label="Photo of a road bicycle" style="background:linear-gradient(160deg,#ffffff,#dfe6ea 50%,#8fa8b8)"></div>
  <div class="meta"><svg width="14" height="14" viewBox="0 0 14 14"><circle cx="7" cy="7.5" r="5.5" stroke="#fff" stroke-width="1.4" fill="none"/><path d="M7 4.5v3" stroke="#fff" stroke-width="1.4"/></svg>03 DEC 2013 <svg width="12" height="12" viewBox="0 0 12 12"><path d="M2 10l1-3 6-6 2 2-6 6z" fill="#fff"/></svg>LORE IPSUM</div>
  <h3>November 18 Cedar<br>Marsh</h3>
  <p style="top:208px">Lorem ipsum sed do dolore magna&nbsp; aliqua minim veniam,.</p>
</div>
<div class="card event-card" style="left:866px;top:845px">
  <div class="photo" role="img" aria-label="Photo of a Paris street with classic buildings" style="background:linear-gradient(170deg,#d9d3c4,#b6a98e 45%,#6d6658)"></div>
  <div class="meta"><svg width="14" height="14" viewBox="0 0 14 14"><circle cx="7" cy="7.5" r="5.5" stroke="#fff" stroke-width="1.4" fill="none"/><path d="M7 4.5v3" stroke="#fff" stroke-width="1.4"/></svg>03 DEC 2013 <svg width="12" height="12" viewBox="0 0 12 12"><path d="M2 10l1-3 6-6 2 2-6 6z" fill="#fff"/></svg>LORE IPSUM</div>
  <h3>November 19 Seabrook</h3>
  <p style="top:208px">Lorem ipsum sed do dolore magna&nbsp; aliqua minim veniam,.</p>
</div>

<!-- footer -->
<footer>
  <nav class="footer-nav abs">Post Your event<span>|</span>Add Auction items<span>|</span>About<span>|</span>Contact</nav>
  <p class="copyright abs">Copyright © 2014 All Rights Reserved | Privacy Policy</p>
  <div class="footer-brand abs"><span class="brand-dot"></span>GivingHost.com</div>
</footer>

</body>
</html>
```